Car wrap for landscaping/gardening company (in Portuguese)

This is a landscaping company that is fully electric, providing, silent, emissions-free landscaping to the community. I am requesting a wrap for the residential van that will be used for this service.

The key things that the wrap must convey, besides the logo of the company, is:
(1) 100% electric (100% Elétrico)
(2) Silent (Silencioso)
(3) No emissions (Sem Emissões)
I envision three large, round icons with a simple image illustrating each of these concepts, and below each icon the text in Portuguese. The van only has to have the logo and the icons, plus a space for phone number and website which can be a little smaller. Use bold colors, make it modern. Don't make it flowery, that will not distinguish the van.

An additional icon can also be added for Customer Service. So possibly 4 icons, with the 4th one saying "Serviço ao Cliente." I am interested in seeing alternatives with 3 and 4 icons.

Please check out the sample that I sent. I like this wrap because it is simple and very visible. It has a lot of text in the rear though which is difficult to read. I don't want this kind of text. Just the icons and the titles. Make it super clear.

The service is high tech, innovative, and premium. It is not a normal landscaping company. I want to attract high end customers who demand the best, who want landscaping that is silent and clean for the environment.

Target Market(s)

Residential customers with patios, large houses, looking for high tech landscaping service and willing to pay a premium

Industry/Entity Type

Landscaping, Gardening

Font styles to use
Sans Serif

Requirements
Must have
• Please use the logo that I have provided. I also need three icons, well displayed, each one representing an aspect of our service: (1) 100% ELÉTRICO (2) SILENCIOSO (3) SEM EMISSÕES. In Portuguese it means 100% electric, Silent, No emissions. Can be three round icons below the logo, very prominent so that people know what the service is about. Also need a place to put two phone numbers, on the back and on the door, as well as the website.
Nice to have
• The picture that I showed is a good example of a blue car wrap. This can work but has to be in green or brown (landscaping colors). I like it because it is bold and visible, and doesn't have too many decorative features. It is very modern and simple, which is consistent with the theme that I am looking for.
Should not have
• Flowery shapes, too much decoration, curvy lines, excessive text

```html
<!DOCTYPE html>
<html lang="pt">
<head>
<meta charset="utf-8">
<title>Verde Calmo – Van Wrap</title>
<link rel="stylesheet" href="https://fonts.googleapis.com/css2?family=Montserrat:wght@500;700;800&family=Oswald:wght@600&display=swap">
<style>
  :root {
    --wrap-green: #1c9a35;
    --wrap-brown: #8a5a36;
    --wrap-white: #ffffff;
    --page-bg: #eef0f1;
    --faint-green: #2aa843;
  }
  html, body {
    margin: 0;
    padding: 0;
    width: 1200px;
    height: 1200px;
    overflow: hidden;
    background: var(--page-bg);
  }
  .canvas {
    position: relative;
    width: 1200px;
    height: 1200px;
  }
  .wrap-panel {
    position: absolute;
    left: 50px;
    top: 390px;
    width: 1100px;
    height: 420px;
    border-radius: 28px;
    overflow: hidden;
    box-shadow: 0 6px 24px rgba(0,0,0,0.08);
  }
  .wrap-panel svg { display: block; }
  .feature-label {
    font-family: "Oswald", "Arial Narrow", sans-serif;
    font-weight: 600;
    font-size: 21px;
    fill: var(--wrap-green);
    letter-spacing: 0.2px;
  }
  .brand-name {
    font-family: "Montserrat", Arial, sans-serif;
    font-weight: 800;
    font-size: 54px;
    fill: var(--wrap-green);
    letter-spacing: 1px;
  }
  .phone-number {
    font-family: "Montserrat", Arial, sans-serif;
    font-weight: 700;
    font-size: 24px;
    fill: var(--wrap-brown);
    letter-spacing: 1px;
  }
  .website {
    font-family: "Montserrat", Arial, sans-serif;
    font-weight: 700;
    font-size: 21px;
    fill: var(--wrap-white);
    letter-spacing: 3px;
  }
  .rear-brand {
    font-family: "Montserrat", Arial, sans-serif;
    font-weight: 800;
    font-size: 64px;
    fill: var(--faint-green);
    letter-spacing: 2px;
  }
  .icon-ring { fill: none; stroke: var(--wrap-brown); stroke-width: 3; }
  .icon-mark { fill: var(--wrap-brown); }
  .icon-line { fill: none; stroke: var(--wrap-brown); stroke-width: 2.6; stroke-linecap: round; stroke-linejoin: round; }
</style>
</head>
<body>
<main class="canvas">
  <section class="wrap-panel" aria-label="Verde Calmo van side wrap">
    <svg width="1100" height="420" viewBox="0 0 1100 420" xmlns="http://www.w3.org/2000/svg">
      <rect class="panel-base" x="0" y="0" width="1100" height="420" fill="var(--wrap-white)"/>

      <!-- rear and lower sweep -->
      <path class="sweep-green"
            d="M790,0 C880,40 905,170 860,245 C815,305 690,322 285,330 L265,420 L1100,420 L1100,0 Z"
            fill="var(--wrap-green)"/>
      <path class="sweep-gap"
            d="M775,0 C866,42 890,168 846,240 C802,298 680,313 280,318"
            fill="none" stroke="var(--wrap-white)" stroke-width="10"/>
      <path class="sweep-stripe"
            d="M758,0 C850,44 874,166 832,235 C790,290 672,303 276,306"
            fill="none" stroke="var(--wrap-brown)" stroke-width="13"/>

      <!-- faint rear name -->
      <text class="rear-brand" transform="translate(1010,30) rotate(90)">VERDE CALMO</text>

      <!-- feature list -->
      <g class="feature-list">
        <g class="feature" transform="translate(628,45)">
          <circle class="icon-ring" cx="0" cy="0" r="15"/>
          <path class="icon-mark" d="M3,-10 L-6,2 L0,2 L-3,10 L6,-2 L0,-2 Z"/>
          <text class="feature-label" x="26" y="8">100% ELÉTRICO</text>
        </g>
        <g class="feature" transform="translate(628,82)">
          <circle class="icon-ring" cx="0" cy="0" r="15"/>
          <path class="icon-mark" d="M-9,-3 L-5,-3 L0,-8 L0,8 L-5,3 L-9,3 Z"/>
          <path class="icon-line" d="M3,-3 L8,3 M8,-3 L3,3"/>
          <text class="feature-label" x="26" y="8">SILENCIOSO</text>
        </g>
        <g class="feature" transform="translate(628,119)">
          <circle class="icon-ring" cx="0" cy="0" r="15"/>
          <text x="-9" y="4" font-family="Montserrat, Arial, sans-serif" font-weight="700" font-size="9" fill="var(--wrap-brown)">CO₂</text>
          <path class="icon-line" d="M-10,-10 L10,10"/>
          <text class="feature-label" x="26" y="8">SEM EMISSÕES</text>
        </g>
        <g class="feature" transform="translate(628,156)">
          <circle class="icon-ring" cx="0" cy="0" r="15"/>
          <path class="icon-line" d="M-7,3 L-7,-1 A7,7 0 0 1 7,-1 L7,3"/>
          <rect class="icon-mark" x="-9" y="0" width="4" height="7" rx="1.5"/>
          <rect class="icon-mark" x="5" y="0" width="4" height="7" rx="1.5"/>
          <text class="feature-label" x="26" y="8">SERVIÇO AO CLIENTE</text>
        </g>
      </g>

      <!-- contact and brand -->
      <text class="phone-number" x="86" y="262">555-210-3864</text>
      <text class="brand-name" x="300" y="272">VERDE CALMO</text>
      <text class="website" x="377" y="384">www.verdecalmo.com</text>
    </svg>
  </section>
</main>
</body>
</html>
```